Maplerise Trading Inc. needs an innovative idea for letterhead and visiting cards.

Maplerise Trading Inc. is a Canadian brand since 2007. It is a renown dealer of kids and office furniture locally. Moreover, exporting electric fixtures e.g. switches, LED's, down-lights etc. to Middle East and Africa. We have initiated a number of steps including re-branding, to boost our export in 2020. We have successfully designed our new logo a few months ago through 'Artfolio' and now we are looking for an innovative idea for a letterhead.
Some key points:
• Red, black and white are the three colors used in all our packaging and furniture. (grey is optional)
• Shouldn’t be too wide.
• Use of watermark is preferable.
• You can visit our North American site at www.mapleriseinc.com. Export website of the company will be launched soon. www.mapleriseinc.ca
• Same letterhead will be used locally and internationally.
• Our new logo and sample packaging is attached.

```html
<!DOCTYPE html>
<html lang="en">
<head>
<meta charset="utf-8">
<title>Maplerise Trading Inc. — Letterhead</title>
<link href="https://fonts.googleapis.com/css2?family=Lato:wght@400;700&family=Questrial&display=swap" rel="stylesheet">
<style>
  :root {
    --brand-red: #a51c24;
    --ink-grey: #4a4a4c;
    --watermark: #ebd0c4;
    --paper: #ffffff;
  }
  * { margin: 0; padding: 0; box-sizing: border-box; }
  html, body { width: 927px; height: 1200px; overflow: hidden; background: var(--paper); }
  .letterhead { position: relative; width: 927px; height: 1200px; background: var(--paper); overflow: hidden; }

  .brand { position: absolute; left: 68px; top: 60px; display: flex; align-items: center; gap: 14px; }
  .brand-square { width: 62px; height: 62px; border: 3px solid var(--brand-red); border-radius: 6px; }
  .brand-name {
    font-family: "Questrial", sans-serif; font-size: 30px; line-height: 32px;
    color: var(--brand-red); letter-spacing: 1px; text-transform: uppercase;
  }

  .watermark {
    position: absolute; left: 150px; top: 420px; width: 566px;
    text-align: center; font-family: "Questrial", sans-serif;
    font-size: 92px; line-height: 104px; color: var(--watermark);
    text-transform: uppercase; letter-spacing: 2px;
  }

  .footer-band {
    position: absolute; left: 0; bottom: 0; width: 927px; height: 56px;
    background: var(--brand-red); color: var(--paper);
    font-family: "Lato", sans-serif; font-size: 12px;
  }
  .contact { position: absolute; top: 0; height: 56px; display: flex; align-items: center; gap: 5px; white-space: nowrap; }
  .contact svg { width: 14px; height: 14px; flex: none; }
  .contact-phone { left: 26px; }
  .contact-email { left: 153px; }
  .contact-web { left: 326px; }
  .contact-address { left: 488px; gap: 14px; line-height: 15px; }
  .footer-square {
    position: absolute; left: 759px; top: -2px; width: 70px; height: 60px;
    background: var(--paper); border: 3px solid var(--brand-red); border-radius: 5px;
    outline: 1px solid var(--paper);
  }
</style>
</head>
<body>
<div class="letterhead">
  <header class="brand">
    <div class="brand-square"></div>
    <div class="brand-name">Maplerise<br>Trading</div>
  </header>

  <div class="watermark" aria-hidden="true">Maplerise<br>Trading</div>

  <footer class="footer-band">
    <div class="contact contact-phone">
      <svg viewBox="0 0 16 16" fill="none" stroke="currentColor" stroke-width="1.4"><circle cx="8" cy="8" r="7"/><path d="M5.5 4.5l1.5 1.6-.8 1.1a5 5 0 0 0 2.6 2.6l1.1-.8 1.6 1.5-.9 1a6 6 0 0 1-6-6z" fill="currentColor" stroke="none"/></svg>
      <span>+1 (888) 555-0147</span>
    </div>
    <div class="contact contact-email">
      <svg viewBox="0 0 16 16" fill="none" stroke="currentColor" stroke-width="1.2"><rect x="1" y="3" width="14" height="10"/><path d="M1 3l7 6 7-6M1 13l5-5M15 13l-5-5"/></svg>
      <span>info@mapleriseinc.com</span>
    </div>
    <div class="contact contact-web">
      <svg viewBox="0 0 16 16" fill="none" stroke="currentColor" stroke-width="1.2"><circle cx="8" cy="8" r="7"/><ellipse cx="8" cy="8" rx="3" ry="7"/><path d="M1 8h14"/></svg>
      <span>www.mapleriseinc.ca</span>
    </div>
    <div class="contact contact-address">
      <svg viewBox="0 0 16 16" fill="currentColor"><path d="M8 1a5 5 0 0 0-5 5c0 4 5 9 5 9s5-5 5-9a5 5 0 0 0-5-5zm0 7a2 2 0 1 1 0-4 2 2 0 0 1 0 4z"/></svg>
      <span>48 Alder Crescent, Unit 210, Markham,<br>ON L3R 0A1</span>
    </div>
    <div class="footer-square"></div>
  </footer>
</div>
</body>
</html>
```